Environmentally conscious Waste Management Company requires business card

We Require a Business card for our environmentally conscious waste management company . The business card should have a very clean design. be double sided and incorporate our logo..
The card will need o have 9 lines for the contact details - that are
Name
Title
Business
Address Line 1
Address Line 2
Address Line 3
Phone
Mobile
Email

Industry/Entity Type

Waste Management

Font styles to use
Other font styles liked:
• Helvetica or similar

```html
<!DOCTYPE html>
<html lang="en">
<head>
<meta charset="utf-8">
<title>Tidyloop Waste – Business Card</title>
<link rel="stylesheet" href="https://fonts.googleapis.com/css2?family=Open+Sans:wght@300;400;700&display=swap">
<style>
  :root {
    --bg: #eceeec;
    --card-white: #ffffff;
    --green: #4cc35f;
    --green-block: #6fcf7f;
    --green-light: #8ddc97;
    --green-dark: #1f8a3c;
    --ink: #222222;
    --ink-soft: #555555;
    --tint: rgba(255, 255, 255, 0.22);
  }
  * { box-sizing: border-box; margin: 0; padding: 0; }
  html, body {
    width: 1200px; height: 800px; overflow: hidden;
    background: var(--bg);
    font-family: "Open Sans", Arial, sans-serif;
  }
  .stage {
    position: relative; width: 1200px; height: 800px;
    display: flex; align-items: center; justify-content: center; gap: 60px;
  }
  .card { position: relative; overflow: hidden; box-shadow: 0 6px 20px rgba(0,0,0,0.15); }

  /* Back side */
  .card-back { width: 340px; height: 560px; background: var(--green); }
  .card-back .tile { position: absolute; background: var(--tint); }
  .card-back .tile-1 { left: 40px; top: 40px; width: 190px; height: 160px; }
  .card-back .tile-2 { left: 20px; top: 20px; width: 300px; height: 200px; background: rgba(255,255,255,0.12); }
  .card-back .tile-3 { left: 150px; top: 70px; width: 130px; height: 160px; }
  .card-back .tile-4 { left: 160px; top: 200px; width: 150px; height: 120px; }
  .card-back .wordmark-vertical {
    position: absolute; left: 140px; top: 70px;
    writing-mode: vertical-rl;
    font-weight: 300; font-size: 82px; line-height: 1; letter-spacing: -1px;
    color: var(--green-dark);
  }

  /* Front side */
  .card-front { width: 560px; height: 340px; background: var(--card-white); }
  .block { position: absolute; background: var(--green-block); }
  .block-top { left: 150px; top: 0; width: 150px; height: 42px; background: var(--green-light); }
  .block-main { left: 0; top: 48px; width: 215px; height: 135px; }
  .block-strip { left: 0; top: 183px; width: 28px; height: 80px; }
  .wordmark {
    position: absolute; left: 170px; top: 56px;
    font-weight: 300; font-size: 54px; letter-spacing: -1px; line-height: 1;
    color: var(--green-dark);
  }
  .contact { position: absolute; left: 6px; top: 196px; list-style: none; }
  .contact li {
    display: flex; align-items: center; gap: 10px;
    font-size: 12.5px; color: var(--ink); height: 19px;
  }
  .contact .icon {
    width: 14px; height: 14px; background: var(--card-white);
    display: flex; align-items: center; justify-content: center;
  }
  .contact .icon svg { width: 10px; height: 10px; }
  .contact li.email { padding-left: 24px; }

  .identity { position: absolute; right: 36px; top: 196px; text-align: right; }
  .identity .name { font-weight: 700; font-size: 18px; color: var(--green); text-transform: uppercase; letter-spacing: 0.3px; }
  .identity .title { font-size: 12.5px; color: var(--ink); margin-bottom: 8px; }
  .identity .business { font-weight: 700; font-size: 13px; color: var(--green); }
  .identity .address { font-size: 13px; color: var(--ink-soft); line-height: 1.35; }
</style>
</head>
<body>
<main class="stage">
  <section class="card card-back" aria-label="Card back">
    <div class="tile tile-2"></div>
    <div class="tile tile-1"></div>
    <div class="tile tile-3"></div>
    <div class="tile tile-4"></div>
    <div class="wordmark-vertical">tidyloop</div>
  </section>

  <section class="card card-front" aria-label="Card front">
    <div class="block block-top"></div>
    <div class="block block-main"></div>
    <div class="block block-strip"></div>
    <div class="wordmark">tidyloop</div>

    <ul class="contact">
      <li>
        <span class="icon"><svg viewBox="0 0 10 10"><rect x="2.5" y="0.5" width="5" height="9" rx="1" fill="none" stroke="#4cc35f" stroke-width="1.2"/></svg></span>
        041 2358 604
      </li>
      <li>
        <span class="icon"><svg viewBox="0 0 10 10"><path d="M2 1 L4 1 L4.6 3.4 L3.4 4.4 Q4.6 6.4 6 6.8 L7 5.6 L9 6.2 L9 8.4 Q5 9 2.4 5.6 Q1 3.4 2 1 Z" fill="#4cc35f"/></svg></span>
        097 1436 285
      </li>
      <li class="email">alexh@tidyloop.com.au</li>
    </ul>

    <div class="identity">
      <p class="name">Alex Harlow</p>
      <p class="title">Director</p>
      <p class="business">Tidyloop Waste</p>
      <p class="address">Shop 3/7 Marlow Place<br>Marlow NT 0814</p>
    </div>
  </section>
</main>
</body>
</html>
```